Educational Agency in Abu Dhabi looking for an 8 pages website

We are looking for an 8 pages design for a website, we already have one but we need to refine it and it is www.korvalendi.ae - Please base it on logo colours (attached) I have uploaded our logo, website content logo colors to use it for the scheme.
We are looking for a smooth look and content added if possible, I also attached content and logo

Industry/Entity Type

Education

Coding

Coded - Design and coding required

Number of Pages Required

5+ page

```html
<!DOCTYPE html>
<html lang="en">
<head>
<meta charset="utf-8">
<title>Korvalendi – Academic Service</title>
<link href="https://fonts.googleapis.com/css2?family=Heebo:wght@500;700;800&family=Lato:wght@400;700&display=swap" rel="stylesheet">
<style>
  :root {
    --indigo: #4350b0;
    --navy: #1f3060;
    --ink: #1e1e24;
    --heading: #2c3050;
    --sky: #079bd0;
    --orange: #fb8c24;
    --yellow: #f6c532;
    --link-blue: #1aa3dc;
    --muted: #a4acc4;
    --white: #ffffff;
  }
  * { margin: 0; padding: 0; box-sizing: border-box; }
  html, body { width: 1200px; height: 1163px; overflow: hidden; background: var(--white); }
  body { position: relative; font-family: "Lato", sans-serif; }

  .top-bar {
    position: absolute; left: 0; top: 0; width: 1200px; height: 27px;
    background: var(--indigo);
  }
  .top-bar nav {
    position: absolute; right: 178px; top: 0; height: 27px;
    display: flex; gap: 12px; align-items: center;
    font-family: "Heebo", sans-serif; font-weight: 500; font-size: 10.5px;
    color: var(--white); letter-spacing: 0.1px;
  }

  .site-header {
    position: absolute; left: 0; top: 27px; width: 1200px; height: 69px;
    background: var(--white); z-index: 3;
  }
  .brand-bubble {
    position: absolute; left: 132px; top: 20px; width: 253px; height: 95px;
    background: var(--white); border-radius: 0 0 127px 127px / 0 0 70px 70px;
    box-shadow: 0 4px 8px rgba(0,0,0,0.12); z-index: 4;
    display: flex; align-items: center; justify-content: center; gap: 8px;
  }
  .brand-bubble .brand-dot { width: 14px; height: 14px; border-radius: 50%; background: var(--navy); }
  .brand-name {
    font-family: "Heebo", sans-serif; font-weight: 800; font-size: 28px;
    color: var(--navy); letter-spacing: 0.5px; margin-top: 10px;
  }
  .brand-dot { margin-top: 10px; }
  .main-nav {
    position: absolute; left: 426px; top: 26px;
    display: flex; gap: 14px;
    font-family: "Heebo", sans-serif; font-weight: 700; font-size: 12px; color: var(--ink);
  }

  .hero-scene { position: absolute; left: 0; top: 96px; width: 1200px; height: 1067px; }

  .hero-title {
    position: absolute; left: 178px; top: 256px;
    font-family: "Heebo", sans-serif; font-weight: 700; font-size: 37px; line-height: 46px;
    color: var(--ink);
  }

  .feature-card {
    position: absolute; top: 546px; width: 270px; height: 176px;
    display: flex; justify-content: center; color: var(--white);
    font-family: "Lato", sans-serif; font-weight: 700; font-size: 13px;
  }
  .feature-card.partners { left: 181px; background: var(--sky); padding-top: 72px; }
  .feature-card.news { left: 466px; background: var(--indigo); padding-top: 80px; }
  .feature-card.apply { left: 750px; background: var(--orange); padding-top: 80px; }

  .feature-text {
    position: absolute; top: 740px; width: 270px; text-align: center;
    font-size: 11.5px; line-height: 18px; color: var(--muted);
  }
  .feature-link {
    position: absolute; top: 813px; width: 270px; text-align: center; font-size: 13px;
  }
  .col-1 { left: 178px; } .col-2 { left: 466px; } .col-3 { left: 750px; }
  .link-yellow { color: var(--yellow); } .link-blue { color: var(--link-blue); }

  .destinations-title {
    position: absolute; left: 0; top: 927px; width: 1200px; text-align: center;
    font-family: "Heebo", sans-serif; font-weight: 700; font-size: 30px; color: var(--heading);
  }
  .flag-row { position: absolute; left: 180px; top: 1008px; display: flex; gap: 24.7px; }
  .flag { width: 83px; height: 83px; border-radius: 50%; }
  .flag.uk { background: linear-gradient(135deg, #23389a, #d4173a 50%, #23389a); }
  .flag.us { background: linear-gradient(180deg, #23389a 40%, #d4173a 40%, #ffffff 60%, #d4173a); }
  .flag.au { background: #2343a0; }
  .flag.my { background: linear-gradient(180deg, #23389a 45%, #d4173a 45%, #ffffff 70%, #d4173a); }
  .flag.eu { background: #1d4aa8; }
  .flag.nz { background: #2343a0; }
  .flag.cn { background: #e0142a; }
  .flag.de { background: linear-gradient(180deg, #111111 33%, #dd0000 33%, #dd0000 66%, #ffcc00 66%); }
</style>
</head>
<body>
  <div class="top-bar">
    <nav><span>ABOUT US</span><span>APPLY NOW</span><span>CONTACT US</span><span>STUDY DESTINATIONS</span></nav>
  </div>

  <svg class="hero-scene" viewBox="0 96 1200 1067" width="1200" height="1067" aria-hidden="false">
    <defs>
      <linearGradient id="photoTone" x1="0" y1="0" x2="1" y2="0">
        <stop offset="0" stop-color="#f6ead6"/>
        <stop offset="0.35" stop-color="#efd7ae"/>
        <stop offset="0.55" stop-color="#6f95b0"/>
        <stop offset="0.75" stop-color="#c98a5c"/>
        <stop offset="1" stop-color="#f0b43a"/>
      </linearGradient>
    </defs>
    <rect role="img" aria-label="Photo of smiling students chatting with books in a bright hallway" x="0" y="96" width="1200" height="600" fill="url(#photoTone)"/>
    <path d="M0,628 Q600,560 1200,664 L1200,944 Q700,860 0,912 Z" fill="var(--navy)"/>
  </svg>

  <header class="site-header">
    <nav class="main-nav">
      <span>ABOUT US</span><span>WHY STUDY ABROAD</span><span>OUR SERVICES</span><span>COURSES</span><span>STUDY ENGLISH LANGUAGE</span><span>SCHOLARSHIPS</span>
    </nav>
  </header>
  <div class="brand-bubble"><span class="brand-dot"></span><span class="brand-name">KORVALENDI</span></div>

  <h1 class="hero-title">You Academic<br>dreams is our<br>important choice</h1>

  <div class="feature-card partners">OUR PARTNERS</div>
  <div class="feature-card news">NEWS &amp; UPDATES</div>
  <div class="feature-card apply">MAKE AN APPLICATION</div>

  <p class="feature-text col-1">At Brightway, our focus is on developing and mastering executive functioning skills necessary to thrive throughout life: Organization,</p>
  <p class="feature-text col-2">Coaches are selected based on a number of crite-ria, including academic achievement, experience, communication skills, individuality, &amp; personality.</p>
  <p class="feature-text col-3">Executive Functioning skills are important for everyone, especially for students with learning differences (such as: ADD, ADHD, Dyslexia.</p>

  <a class="feature-link col-1 link-yellow">Learn More</a>
  <a class="feature-link col-2 link-blue">Learn More</a>
  <a class="feature-link col-3 link-yellow">Learn More</a>

  <h2 class="destinations-title">Study Destinations</h2>
  <div class="flag-row">
    <div class="flag uk" role="img" aria-label="United Kingdom flag"></div>
    <div class="flag us" role="img" aria-label="United States flag"></div>
    <div class="flag au" role="img" aria-label="Australia flag"></div>
    <div class="flag my" role="img" aria-label="Malaysia flag"></div>
    <div class="flag eu" role="img" aria-label="European Union flag"></div>
    <div class="flag nz" role="img" aria-label="New Zealand flag"></div>
    <div class="flag cn" role="img" aria-label="China flag"></div>
    <div class="flag de" role="img" aria-label="Germany flag"></div>
  </div>
</body>
</html>
```